Flyer Design

I need a nice professional flyer design to use for advertising my lawn/snow removal business. Flyers I am using are 5.47"x4.21". I've attached a flyer I found online that I liked. Just wanting something creative and professional. The images of the logos I attached are of the original logo design, and the new color design we are using. There is also a mockup of our tshirt design to give you an idea of the actual color on the tshirt, since the jpeg logo isn't exactly accurate on color.
Things I need on the flyer in no particular order:
"Snow is coming"
"Don't Wait Until It's TOO LATE!"
"Free Estimates"
Services offered
"Commercial/Residential"
"Snow Plowing"
"Snow Blowing"
"Snow Shoveling"
"Ice Removal"
"Salting/Sanding"
"Fully Licensed and Insured"
"Available and ON CALL 24/7"
"Seasonal Packages Available"
"CALL NOW TO RESERVE"

```html
<!DOCTYPE html>
<html lang="en">
<head>
<meta charset="utf-8">
<title>Snow Removal Flyer</title>
<link href="https://fonts.googleapis.com/css2?family=Cinzel:wght@700;900&family=Poppins:wght@600&family=Oswald:wght@500&display=swap" rel="stylesheet">
<style>
  :root{
    --orange:#fb4a08;
    --black:#121212;
    --white:#ffffff;
    --stage:#3a3a3a;
    --snow-light:#e6ecf2;
    --snow-sky:#9fb4cc;
  }
  html,body{margin:0;padding:0;overflow:hidden;}
  body{width:1200px;height:907px;background:var(--stage);position:relative;}
  .flyer{position:absolute;left:122px;top:75px;width:983px;height:755px;background:var(--black);overflow:hidden;}
  .flyer-shapes{position:absolute;left:0;top:0;}
  .brand{position:absolute;left:63px;top:15px;width:170px;height:170px;border-radius:50%;background:var(--white);
    display:flex;flex-direction:column;align-items:center;justify-content:center;
    font-family:"Oswald",sans-serif;font-weight:500;color:var(--black);text-transform:uppercase;text-align:center;line-height:1.05;}
  .brand-name{font-size:30px;}
  .brand-sub{font-size:15px;letter-spacing:1px;}
  .headline{position:absolute;left:58px;top:360px;width:740px;text-align:center;margin:0;
    font-family:"Cinzel",serif;font-weight:900;font-variant:small-caps;color:var(--white);font-size:72px;line-height:1;letter-spacing:1px;}
  .subline{position:absolute;left:58px;top:443px;width:740px;text-align:center;margin:0;
    font-family:"Cinzel",serif;font-weight:700;font-variant:small-caps;color:var(--orange);font-size:38px;line-height:1;}
  .services-title{position:absolute;right:20px;top:497px;margin:0;font-family:"Poppins",sans-serif;font-weight:600;
    font-size:29px;color:var(--white);text-decoration:underline;text-underline-offset:4px;text-decoration-thickness:2px;}
  .service-list{position:absolute;left:20px;top:547px;width:950px;margin:0;padding:0;list-style:none;
    display:grid;grid-template-columns:400px 292px 258px;row-gap:8px;
    font-family:"Poppins",sans-serif;font-weight:600;font-size:21px;color:var(--white);line-height:27px;}
  .service-list li::before{content:"\2605";margin-right:4px;font-size:18px;}
  .service-list li:nth-child(1){grid-column:1;grid-row:1}
  .service-list li:nth-child(2){grid-column:1;grid-row:2}
  .service-list li:nth-child(3){grid-column:2;grid-row:1}
  .service-list li:nth-child(4){grid-column:2;grid-row:2}
  .service-list li:nth-child(5){grid-column:3;grid-row:1}
  .service-list li:nth-child(6){grid-column:3;grid-row:2}
  .assurances{position:absolute;left:83px;top:660px;margin:0;font-family:"Oswald",sans-serif;font-weight:500;
    font-size:25px;color:var(--white);text-transform:uppercase;line-height:37px;}
  .assurances p{margin:0;}
  .call-block{position:absolute;left:560px;top:650px;width:420px;text-align:center;font-family:"Oswald",sans-serif;font-weight:500;text-transform:uppercase;}
  .availability{margin:0;font-size:23px;color:var(--white);line-height:30px;}
  .cta{margin:0;font-size:44px;color:var(--orange);line-height:54px;}
</style>
</head>
<body>
  <main class="flyer">
    <svg class="flyer-shapes" width="983" height="755" viewBox="0 0 983 755">
      <path d="M150,17 H983 V347 H290 C200,340 140,270 140,185 C140,110 150,50 150,17 Z" fill="var(--orange)"/>
      <path d="M300,35 H983 V347 H330 C260,330 205,270 205,190 C205,110 250,55 300,35 Z" fill="var(--snow-sky)"/>
      <rect x="790" y="347" width="193" height="150" fill="var(--orange)"/>
      <rect x="0" y="490" width="983" height="265" fill="var(--orange)"/>
      <path d="M0,347 H805 A72,72 0 0 1 805,490 H0 Z" fill="var(--black)"/>
      <path d="M103,635 H983 V745 H103 A55,55 0 0 1 103,635 Z" fill="var(--black)"/>
    </svg>
    <svg class="flyer-shapes" width="983" height="755" viewBox="0 0 983 755" role="img" aria-label="Photo of a red snow groomer on a mountain ski slope">
      <defs>
        <linearGradient id="snowPhoto" x1="0" y1="0" x2="0" y2="1">
          <stop offset="0" stop-color="var(--snow-sky)"/>
          <stop offset="1" stop-color="var(--snow-light)"/>
        </linearGradient>
      </defs>
      <path d="M300,35 H983 V347 H330 C260,330 205,270 205,190 C205,110 250,55 300,35 Z" fill="url(#snowPhoto)"/>
    </svg>

    <div class="brand">
      <span class="brand-name">Northfield</span>
      <span class="brand-sub">Lawn &amp; Landscape</span>
    </div>

    <h1 class="headline">Snow is coming</h1>
    <p class="subline">Don't Wait Until It's TOO LATE!</p>

    <h2 class="services-title">Services:</h2>
    <ul class="service-list">
      <li>Commercial/Residential</li>
      <li>Snow Plowing</li>
      <li>Snow Shoveling</li>
      <li>Ice Removal</li>
      <li>Snow Blowing</li>
      <li>Salting/Sanding</li>
    </ul>

    <div class="assurances">
      <p>Fully Licensed and Insured</p>
      <p>Seasonal Packages Available</p>
    </div>

    <div class="call-block">
      <p class="availability">Available and on call 24/7</p>
      <p class="cta">Call now to reserve</p>
    </div>
  </main>
</body>
</html>
```